Stand Tall Always needs a book cover design

I need a book cover design for the following title:
Stand Tall Always-Grow a Bold Captain
Family methods from Cradle through Elder Years
by Dr. Martin P. Olund
I am interviewing a number of strong Canadian Leaders-specifically with regard to their experience of being parented. The book is a reaction today of parents having no backbone, no will nor ability to discipline their children. Many parents want to make a change but don't know how to.
Updates
Title should be "Stand Tall Always-Grow a Bold Captain" the rest is correct Added Wednesday, November 11, 2015
Here is an example of what we would need on the back cover in text only.
What does it take to raise a strong leader? Psychologist Dr. Martin P. Olund provides you with 6 must do strategies based on his 26 years of clinical experience and the interview of 6 strong leaders for this book. Strategies that you can start using today to insure your child’s success.
Target Market(s)
parents and grandparents
Requirements
Must have
- a way to communicate strength in parenting

```html
<!DOCTYPE html>
<html lang="en">
<head>
<meta charset="utf-8">
<title>Stand Tall Always-Grow a Bold Captain — Cover Spread</title>
<link rel="stylesheet" href="https://fonts.googleapis.com/css2?family=Cinzel:wght@500;600;700&family=Questrial&display=swap">
<style>
  :root {
    --page: #ffffff;
    --mint: #e8f1ef;
    --navy: #05213a;
    --ink: #0d1a26;
    --green: #2f8f3a;
    --photo-top: #c9b79d;
    --photo-mid: #e4e0d8;
    --white: #ffffff;
  }
  * { margin: 0; padding: 0; box-sizing: border-box; }
  html, body { width: 1200px; height: 960px; overflow: hidden; background: var(--page); }
  .canvas { position: relative; width: 1200px; height: 960px; }

  .spread { position: absolute; left: 50px; top: 110px; width: 1100px; height: 740px; background: var(--mint); overflow: hidden; }

  /* Back cover */
  .back { position: absolute; left: 0; top: 0; width: 500px; height: 740px; }
  .back-title {
    position: absolute; left: 0; top: 58px; width: 500px; text-align: center;
    font-family: "Cinzel", serif; font-weight: 600; color: var(--navy);
    font-size: 30px; line-height: 32px; white-space: nowrap;
  }
  .blurb {
    position: absolute; left: 40px; top: 170px; width: 420px;
    font-family: "Questrial", sans-serif; font-size: 12.6px; line-height: 16.6px;
    color: var(--ink); text-align: justify;
  }
  .blurb p { text-indent: 28px; }
  .back-rule { position: absolute; left: 40px; top: 389px; width: 420px; height: 2px; background: var(--navy); }
  .author-photo { position: absolute; left: 40px; top: 400px; width: 125px; height: 127px; background: var(--navy); }
  .bio {
    position: absolute; left: 40px; top: 400px; width: 420px;
    font-family: "Questrial", sans-serif; font-size: 12.6px; line-height: 16.6px;
    color: var(--ink); text-align: justify;
  }
  .bio .float-gap { float: left; width: 142px; height: 128px; }
  .bio p { text-indent: 28px; }
  .bio .author-name { font-style: italic; font-size: 14px; }
  .bio .caps { font-style: italic; font-size: 10px; }
  .back-band { position: absolute; left: 0; top: 632px; width: 500px; height: 108px; background: var(--navy); }
  .code-box { position: absolute; left: 57px; top: 648px; width: 108px; height: 72px; background: var(--white); }

  /* Spine + front photo */
  .cover-photo {
    position: absolute; left: 500px; top: 0; width: 600px; height: 470px;
    background: linear-gradient(180deg, var(--photo-top) 0%, var(--photo-mid) 12%, #dcdcd4 55%, var(--mint) 100%);
  }
  .spine-title {
    position: absolute; left: 518px; top: 52px; height: 460px;
    writing-mode: vertical-rl;
    font-family: "Cinzel", serif; font-weight: 600; color: var(--navy);
    font-size: 28px; line-height: 34px; white-space: nowrap;
  }
  .spine-author {
    position: absolute; left: 541px; top: 525px;
    writing-mode: vertical-rl;
    font-family: "Cinzel", serif; font-weight: 600; color: var(--navy);
    font-size: 27px; white-space: nowrap;
  }

  /* Front */
  .front-title {
    position: absolute; left: 600px; top: 374px; width: 500px; text-align: center;
    font-family: "Cinzel", serif; font-weight: 600; color: var(--navy);
    font-size: 45px; line-height: 49px; white-space: nowrap;
  }
  .front-subtitle {
    position: absolute; left: 600px; top: 547px; width: 500px; text-align: center;
    font-family: "Cinzel", serif; font-weight: 600; color: var(--green);
    font-size: 18.5px; line-height: 21px;
  }
  .front-author {
    position: absolute; left: 600px; top: 652px; width: 500px; text-align: center;
    font-family: "Cinzel", serif; font-weight: 700; color: var(--ink);
    font-size: 34px; white-space: nowrap;
  }
</style>
</head>
<body>
<div class="canvas">
  <div class="spread">

    <section class="back">
      <h2 class="back-title">Stand Tall Always-Grow<br>a Bold Captain</h2>
      <div class="blurb">
        <p>What does it take to raise a strong leader? Psychologist Dr. Martin P. Olund provides you with 6 must do strategies based on his 26 years of clinical experience and the interview of 6 strong leaders for this book. Strategies that you can start using today to insure your child’s success.</p>
        <p>What does it take to raise a strong leader? Psychologist Dr. Martin P. Olund provides you with 6 must do strategies based on his 26 years of clinical experience and the interview of 6 strong leaders for this book. Strategies that you can start using today to insure your child’s success.</p>
        <p>What does it take to raise a strong leader? Psychologist Dr. Martin P. Olund provides you with 6 must do strategies based on his 26 years of clinical experience and the interview of 6 strong leaders for this book. Strategies that you can start using today to insure your child’s success.</p>
      </div>
      <div class="back-rule"></div>
      <div class="author-photo" role="img" aria-label="Author portrait placeholder"></div>
      <div class="bio">
        <div class="float-gap"></div>
        <p><span class="author-name">Dr. Martin P. Olund</span> <span class="caps">IS</span> What does it take to raise a strong leader? Psychologist Dr. Martin P. Olund provides you with 6 must do strategies based on his 26 years of clinical experience and the interview of 6 strong leaders for this book. Strategies that you can start using today to insure your child’s success.</p>
        <p>What does it take to raise a strong leader? Psychologist Dr. Martin P. Olund provides you with 6 must do strategies based on his 26 years of clinical experience and the interview of 6 strong leaders for this book. Strategies that you can start using today to insure your child’s success.</p>
      </div>
      <div class="back-band"></div>
      <div class="code-box"></div>
    </section>

    <div class="cover-photo" role="img" aria-label="Photo of a smiling mother lying on a soft rug with a toddler holding a marker and a crawling baby, drawing together among colourful pillows and cups"></div>

    <div class="spine-title">Stand Tall Always-<br>Grow a Bold Captain</div>
    <div class="spine-author">Dr. Martin</div>

    <h1 class="front-title">Stand Tall<br>Always-Grow<br>a Bold Captain</h1>
    <p class="front-subtitle">Family methods<br>from Cradle through Elder Years</p>
    <p class="front-author">by Dr. Martin P. Olund</p>

  </div>
</div>
</body>
</html>
```